Minimalist, Flat(Matte) design for a Beef Jerky packaging company. No bullshit company looking for a

Need a packaging design for a new Beef Jerky product(in English). The name of the company is 'Vellorn' and thus the packaging should reflect the bullish, tough, and simple nature of the beef jerky product. The finished product should communicate simplicity, minimalism, yet toughness and strength.

The logo should be simple, with a minimal number of colors , and should be either all white/cream, or have some red as well. Main colors should be white, cream, tinted red, and matte black. I think 4 colors max would be best. The closest example to an existing package style would be Kessip Noir clove cigarettes( image attached).

It will be on a matte black standing pouch package. See image for package type. Package dimensions:

Dimension: Width x Gusset x Height
INCH : 5.125" (W) x 3.125" (G) x 8.125" (H)
MILLIMETER : 130mm (W) x 80mm (G) x 205mm (H)

I don't have anything totally specific so artistic liberty is encouraged, provided the colors are kept to a minimum and looks consistent with the simple nature of the brand and the matte black packaging.

Also attached an existing beef jerky package with a similar style to what we're looking for.

Industry/Entity Type

It Company

Colors
f59195
ffffff

Requirements
Must have
• Low contrast, flat and minimalist design.
Should not have
• A complicated design with many colors. Gawdy/flashy design. Bright colors. High contrast.

```html
<!DOCTYPE html>
<html lang="en">
<head>
<meta charset="utf-8">
<title>Vellorn Beef Jerky – Pouch Front</title>
<link rel="stylesheet" href="https://fonts.googleapis.com/css2?family=Anton&family=Fjalla+One&family=Oswald:wght@400&display=swap">
<style>
  :root {
    --backdrop: #e4e4e4;
    --pouch-black: #1d1d1f;
    --pouch-edge: #151516;
    --accent-red: #c8242b;
    --ink-white: #ffffff;
    --ink-soft: #e9e9e9;
  }
  html, body {
    margin: 0;
    padding: 0;
    width: 1200px;
    height: 1200px;
    overflow: hidden;
    background: var(--backdrop);
  }
  .canvas {
    position: relative;
    width: 1200px;
    height: 1200px;
  }
  .pouch-front {
    position: absolute;
    left: 305px;
    top: 95px;
    width: 620px;
    height: 1025px;
    background: var(--pouch-black);
    box-shadow: inset 0 0 0 14px var(--pouch-edge);
  }
  .zip-seal {
    position: absolute;
    left: 14px;
    right: 14px;
    top: 110px;
    height: 2px;
    background: #2a2a2c;
  }
  .rule {
    position: absolute;
    height: 2px;
    background: var(--accent-red);
  }
  .rule--top-left { left: 14px; width: 220px; top: 313px; }
  .rule--top-right { left: 410px; right: 14px; top: 313px; }
  .rule--bottom { left: 14px; right: 14px; top: 833px; }
  .emblem-area {
    position: absolute;
    left: 204px;
    top: 232px;
    width: 222px;
    height: 90px;
    display: block;
  }
  .brand-name {
    position: absolute;
    left: 0;
    right: 0;
    top: 430px;
    margin: 0;
    text-align: center;
    font-family: "Anton", "Impact", sans-serif;
    font-weight: 400;
    font-size: 118px;
    line-height: 1;
    letter-spacing: 4px;
    color: var(--ink-white);
  }
  .product-name {
    position: absolute;
    left: 0;
    right: 0;
    top: 665px;
    margin: 0;
    text-align: center;
    font-family: "Fjalla One", sans-serif;
    font-size: 50px;
    line-height: 1;
    letter-spacing: 3px;
    color: var(--ink-soft);
  }
  .net-weight {
    position: absolute;
    left: 0;
    right: 0;
    top: 888px;
    margin: 0;
    text-align: center;
    font-family: "Oswald", sans-serif;
    font-size: 32px;
    line-height: 1;
    color: var(--ink-soft);
  }
</style>
</head>
<body>
<main class="canvas">
  <section class="pouch-front">
    <div class="zip-seal"></div>
    <div class="rule rule--top-left"></div>
    <div class="rule rule--top-right"></div>
    <svg class="emblem-area" role="img" aria-label="Running bull silhouette illustration" viewBox="0 0 222 90">
      <rect x="0" y="0" width="222" height="90" fill="#ffffff" fill-opacity="0.85"/>
    </svg>
    <h1 class="brand-name">VELLORN</h1>
    <p class="product-name">BEEF JERKY</p>
    <div class="rule rule--bottom"></div>
    <p class="net-weight">NET WT 3OZ</p>
  </section>
</main>
</body>
</html>
```